Verelin Publishing

I made a website myself www.verelinpublishing.co.uk a few years ago but I need a new design, which I will code. One that I can be proud of, that 's sexy, to win new customers and showcase my publishing skills. This is a publishing website so I want the home page and books page to be fantastic. I have a logo already so will like the same colour scheme or thereabouts. I have current files and features that I would like to add to your creativity and experience.

Target Market(s)

Web Designers, Graphic Designers

Industry/Entity Type

Book Publisher

Number of Pages Required

5+ page

Font styles to use
Sans Serif

Colors
0255a3
ffffff
ec1f27

Requirements
Must have
• Menu and Sub Menu
• Footer
• Buy Page - Shopping Cart
• Upload feature on the submissions page
• video section on home page (how we publish books)
• Ad space section
Nice to have
• social media bar
• Zoom in page

```html
<!DOCTYPE html>
<html lang="en">
<head>
<meta charset="utf-8">
<title>Verelin Publishing</title>
<link href="https://fonts.googleapis.com/css2?family=Roboto:wght@400;500;700&display=swap" rel="stylesheet">
<style>
:root{
  --navy:#15123f;
  --blue:#0255a3;
  --red:#ec1f27;
  --white:#ffffff;
  --ink:#222222;
  --grey-band:#808080;
  --line:#0255a3;
}
*{margin:0;padding:0;box-sizing:border-box}
html,body{width:1200px;height:2769px;overflow:hidden;background:var(--white)}
body{position:relative;font-family:'Roboto',Arial,sans-serif;color:var(--ink)}
.abs{position:absolute}

/* header */
.topbar{left:0;top:0;width:1200px;height:55px;background:var(--navy)}
.brand-badge{left:148px;top:0;width:83px;height:107px;background:var(--white);border-radius:0 0 42px 42px;border-left:4px solid var(--red);border-bottom:4px solid var(--red);z-index:5;display:flex;flex-direction:column;align-items:center;justify-content:flex-end;padding-bottom:16px}
.brand-badge .dot{width:22px;height:22px;border-radius:50%;background:var(--red);margin-bottom:8px}
.brand-badge .brand-name{font-size:11px;font-weight:700;color:var(--blue);text-align:center;line-height:12px}
.main-nav{left:0;top:0;height:55px;width:1200px}
.main-nav a{position:absolute;top:16px;font-size:14px;font-weight:500;color:var(--white);text-decoration:none;line-height:22px}
.main-nav a.active{background:var(--red);border-radius:12px;padding:0 18px}

/* hero */
.hero{left:0;top:55px;width:1200px;height:370px;background:linear-gradient(90deg,#8a5a37 0%,#b58459 30%,#d9d4cf 55%,#9c9894 72%,#1c1c1c 92%)}
.hero-title{left:150px;top:118px;font-size:56px;font-weight:500;color:var(--white);text-shadow:0 2px 4px rgba(0,0,0,.35)}
.hero-sub{left:150px;top:186px;font-size:39px;font-weight:400;color:var(--white);text-shadow:0 2px 4px rgba(0,0,0,.35)}
.hero-btn{left:150px;top:301px;width:205px;height:46px;background:var(--red);border-radius:23px;color:var(--white);font-size:24px;font-weight:500;display:flex;align-items:center;justify-content:center}

.social-rail{left:0;top:124px;width:35px}
.social-rail span{display:block;width:35px;height:36px;margin-bottom:3px;background:var(--blue)}
.social-rail span:nth-child(4),.social-rail span:nth-child(5),.social-rail span:nth-child(6){background:var(--red)}

/* intro */
.eyebrow{left:0;top:482px;width:1200px;text-align:center;font-size:36px;font-weight:500;color:var(--blue)}
.intro-heading{left:0;top:524px;width:1200px;text-align:center;font-size:39px;font-weight:500;color:var(--ink)}
.intro-text{left:0;top:598px;width:1200px;text-align:center;font-size:15.5px;line-height:29px;color:var(--ink)}
.feature{width:200px;text-align:center}
.feature .icon-box{width:112px;height:114px;margin:0 auto;border:2px solid var(--blue);display:flex;align-items:center;justify-content:center}
.feature .label{margin-top:24px;font-size:28px;font-weight:500;color:var(--red)}

/* video */
.video-band{left:0;top:960px;width:1200px;height:401px;background:linear-gradient(90deg,#2b2b2b,#5b5b5b 40%,#4a4a4a 70%,#3a3a3a)}
.video-title{left:0;top:990px;width:1200px;text-align:center;font-size:36px;font-weight:400;color:var(--white)}
.video-frame{left:312px;top:1063px;width:576px;height:261px;background:linear-gradient(180deg,#a0262c,#8d2026);border:2px solid #e8e8e8;display:flex;align-items:center;justify-content:center}

/* steps */
.steps-title{left:0;top:1398px;width:1200px;text-align:center;font-size:40px;font-weight:500;color:var(--blue)}
.step-spine{left:597px;top:1520px;width:7px;height:320px;background:var(--blue)}
.step{left:164px;width:872px;height:101px;border:2px solid var(--blue);border-radius:50px;background:var(--white);overflow:hidden}
.step .num{position:absolute;left:0;top:0;width:66px;height:100%;background:var(--blue);color:var(--white);font-size:44px;display:flex;align-items:center;justify-content:center;padding-left:8px}
.step .name{position:absolute;left:80px;top:0;height:100%;display:flex;align-items:center;font-size:28px;font-weight:500;color:var(--blue)}
.step .copy{position:absolute;left:297px;top:22px;width:550px;font-size:13px;line-height:21px;color:var(--ink)}

/* partners */
.partners-band{left:0;top:2029px;width:1200px;height:253px;background:var(--grey-band)}
.partners-title{left:0;top:2058px;width:1200px;text-align:center;font-size:40px;color:var(--white)}
.partner-tile{top:2160px;width:140px;height:68px;background:var(--white);border:1px solid #d6d6d6;display:flex;align-items:center;justify-content:center}
.partner-tile span{width:70px;height:18px;border-radius:9px;background:#d9d9d9}

/* testimonials */
.testimonials-title{left:0;top:2314px;width:1200px;text-align:center;font-size:40px;font-weight:500;color:var(--blue)}
.avatar{left:242px;top:2389px;width:140px;height:140px;border-radius:50%;background:linear-gradient(160deg,#7b6a58,#3f4a3c)}
.quote{left:439px;top:2402px;width:520px;font-size:16px;line-height:28px;color:var(--ink)}

/* footer */
.footer{left:0;top:2586px;width:1200px;height:137px;background:var(--navy)}
.footer-badge{left:148px;top:2586px;width:83px;height:109px;background:var(--white);border-radius:0 0 42px 42px;border-left:4px solid var(--red);border-bottom:4px solid var(--red);display:flex;flex-direction:column;align-items:center;justify-content:flex-end;padding-bottom:16px}
.footer-badge .dot{width:22px;height:22px;border-radius:50%;background:var(--red);margin-bottom:8px}
.footer-badge .brand-name{font-size:11px;font-weight:700;color:var(--blue);text-align:center;line-height:12px}
.footer-col{top:2609px;font-size:13px;font-weight:500;color:var(--white);line-height:26px}
.legal-bar{left:0;top:2723px;width:1200px;height:46px;background:var(--blue)}
.legal-text{left:148px;top:2736px;font-size:12px;color:var(--white)}
.legal-social{top:2736px;width:18px;height:18px;border-radius:50%;background:var(--white)}
</style>
</head>
<body>

<header>
  <div class="abs topbar"></div>
  <nav class="abs main-nav">
    <a class="active" style="left:323px">Home</a>
    <a style="left:430px">Publishing</a>
    <a style="left:551px">Submissions</a>
    <a style="left:686px">Books</a>
    <a style="left:780px">Authors</a>
    <a style="left:866px">Seminars</a>
    <a style="left:998px">Contact</a>
  </nav>
  <div class="abs brand-badge"><div class="dot"></div><div class="brand-name">Verelin<br>Publishing</div></div>
</header>

<section>
  <div class="abs hero" role="img" aria-label="Photo of a smiling woman typing on a white laptop in a bright room"></div>
  <h1 class="abs hero-title">Verelin Publishing</h1>
  <p class="abs hero-sub">Self-Publishing that works</p>
  <div class="abs hero-btn">SUBMIT BOOK</div>
  <div class="abs social-rail"><span></span><span></span><span></span><span></span><span></span><span></span></div>
</section>

<section>
  <h2 class="abs eyebrow">HAVE A STORY?</h2>
  <p class="abs intro-heading">We can help you publish your book.</p>
  <p class="abs intro-text">Welcome to Verelin Publishing, we are an independent publishing company located in London/Surrey.<br>We publish Trade (fiction and non-fiction), &amp; Young Adult (YA) books in avariety of subjects</p>

  <div class="abs feature" style="left:247px;top:709px">
    <div class="icon-box">
      <svg width="52" height="60" viewBox="0 0 52 60" fill="none" stroke="#ec1f27" stroke-width="3"><rect x="8" y="4" width="38" height="52" rx="2"/><line x1="4" y1="14" x2="12" y2="14"/><line x1="4" y1="24" x2="12" y2="24"/><line x1="4" y1="34" x2="12" y2="34"/><line x1="4" y1="44" x2="12" y2="44"/><rect x="18" y="14" width="20" height="10"/></svg>
    </div>
    <div class="label">Books</div>
  </div>
  <div class="abs feature" style="left:502px;top:709px">
    <div class="icon-box">
      <svg width="46" height="62" viewBox="0 0 46 62" fill="none" stroke="#ec1f27" stroke-width="3"><path d="M23 4 L38 30 L30 42 H16 L8 30 Z"/><line x1="23" y1="4" x2="23" y2="26"/><circle cx="23" cy="29" r="3"/><rect x="13" y="46" width="20" height="10"/></svg>
    </div>
    <div class="label">Authors</div>
  </div>
  <div class="abs feature" style="left:755px;top:709px">
    <div class="icon-box">
      <svg width="50" height="62" viewBox="0 0 50 62" fill="none" stroke="#ec1f27" stroke-width="3"><rect x="5" y="8" width="40" height="50" rx="2"/><rect x="16" y="3" width="18" height="10" rx="2"/><line x1="13" y1="24" x2="37" y2="24"/><line x1="13" y1="32" x2="37" y2="32"/><line x1="13" y1="40" x2="37" y2="40"/><line x1="13" y1="48" x2="30" y2="48"/></svg>
    </div>
    <div class="label">Submissions</div>
  </div>
</section>

<section>
  <div class="abs video-band" role="img" aria-label="Blurred photo of an office with a computer and bookshelves"></div>
  <h2 class="abs video-title">LEARN HOW WE PUBLISH BOOKS</h2>
  <div class="abs video-frame">
    <svg width="74" height="74" viewBox="0 0 74 74" fill="none"><circle cx="37" cy="37" r="34" stroke="#ffffff" stroke-width="3"/><path d="M29 23 L53 37 L29 51 Z" fill="#ffffff"/></svg>
  </div>
</section>

<section>
  <h2 class="abs steps-title">Publish Your Book in 4 Easy Steps</h2>
  <div class="abs step-spine"></div>
  <div class="abs step" style="top:1479px"><div class="num">1</div><div class="name">WRITING</div><p class="copy">Are you a budding writer waiting to be discovered? Do you believe in yourself and your work? If so then you have come to the right place. We accept unsolicited manuscripts and are currently looking for new authors to publish with.</p></div>
  <div class="abs step" style="top:1606px"><div class="num">2</div><div class="name">SUBMISSION</div><p class="copy">Are you a budding writer waiting to be discovered? Do you believe in yourself and your work? If so then you have come to the right place. We accept unsolicited manuscripts and are currently looking for new authors to publish with.</p></div>
  <div class="abs step" style="top:1733px"><div class="num">3</div><div class="name">REVIEW</div><p class="copy">Are you a budding writer waiting to be discovered? Do you believe in yourself and your work? If so then you have come to the right place. We accept unsolicited manuscripts and are currently looking for new authors to publish with.</p></div>
  <div class="abs step" style="top:1861px"><div class="num">4</div><div class="name">CONTRACT</div><p class="copy">Are you a budding writer waiting to be discovered? Do you believe in yourself and your work? If so then you have come to the right place. We accept unsolicited manuscripts and are currently looking for new authors to publish with.</p></div>
</section>

<section>
  <div class="abs partners-band"></div>
  <h2 class="abs partners-title">Companies we work with</h2>
  <div class="abs partner-tile" style="left:135px"><span></span></div>
  <div class="abs partner-tile" style="left:294px"><span></span></div>
  <div class="abs partner-tile" style="left:452px"><span></span></div>
  <div class="abs partner-tile" style="left:611px"><span></span></div>
  <div class="abs partner-tile" style="left:768px"><span></span></div>
  <div class="abs partner-tile" style="left:925px"><span></span></div>
</section>

<section>
  <h2 class="abs testimonials-title">Testimonials</h2>
  <div class="abs avatar" role="img" aria-label="Portrait photo of a client"></div>
  <p class="abs quote">Are you a budding writer waiting to be discovered? Do you believe in yourself and your work? If so then you have come to the right place. We accept unsolicited manuscripts and are currently looking for new authors to publish with.</p>
</section>

<footer>
  <div class="abs footer"></div>
  <div class="abs footer-badge"><div class="dot"></div><div class="brand-name">Verelin<br>Publishing</div></div>
  <div class="abs footer-col" style="left:386px">Home<br>Publishing<br>Submissions</div>
  <div class="abs footer-col" style="left:587px">Books<br>Ebooks<br>Authors</div>
  <div class="abs footer-col" style="left:764px">Seminars<br>Packages<br>Contact</div>
  <div class="abs legal-bar"></div>
  <p class="abs legal-text">Copyright © 2017 Verelin Publishing. All Rights Reserved.</p>
  <div class="abs legal-social" style="left:948px"></div>
  <div class="abs legal-social" style="left:989px"></div>
  <div class="abs legal-social" style="left:1035px"></div>
</footer>

</body>
</html>
```